Velisa Seafood Shipping Packaging Re-Design

We need a packaging (Shipping Carton) design for our Seafood Products (FROZEN). We already have a basic packaging design which we prefer to have a modern touch on it.
Spec :
1. It must show our logo (Attached), note that the text of "VELISA" which accompany the logo is optional, it can be omitted & showing only the logo.
2. Main color is Blue
3. Our carton is regular shipping box with dimension L43cm x W 27cm x H 16cm.
4. Our material of Carton is both Brown & White Kraft Paperboard, so the design should look nice in both material.

Attached our Logo and packaging design.

Target Market(s)

Frozen Seafood Distributor & Seafood Buyer

Industry/Entity Type

Food Production

Requirements
Must have
• 1. Must Show our Logo
• 2. Main Color of the Text/Logo is Blue
• 3. On the side of the packaging / Carton must show two box of CODE & SIZE
• 4. Must Show these icons :
• a. Handle with Care
• b. Maximum Stackable 10 Carton
• c. Recyleable Material
• d. Protect from the Water/Rain
Nice to have
• Would prefer to have a modern design

```html
<!DOCTYPE html>
<html lang="en">
<head>
<meta charset="utf-8">
<title>Velisa Frozen Fish Carton – Design Options</title>
<link href="https://fonts.googleapis.com/css2?family=Open+Sans:wght@400&family=Montserrat:wght@300;500;600;800&display=swap" rel="stylesheet">
<style>
  :root {
    --navy: #1f3b86;
    --navy-deep: #1a3373;
    --sea: #23b6dc;
    --sea-light: #5fd0ea;
    --aqua-1: #9adfe6;
    --aqua-2: #6fcbd9;
    --ice: #e8f4f8;
    --white: #ffffff;
    --ink: #111111;
  }
  * { box-sizing: border-box; margin: 0; padding: 0; }
  html, body { width: 1200px; height: 1200px; overflow: hidden; background: var(--white); }
  body { position: relative; font-family: "Montserrat", sans-serif; }

  .option-title {
    position: absolute; left: 0; width: 1200px; text-align: center;
    font-family: "Open Sans", sans-serif; font-weight: 400; font-size: 78px;
    color: var(--ink); letter-spacing: 1px; line-height: 1;
  }
  .option-title--one { top: 28px; }
  .option-title--two { top: 610px; }

  .carton-panel { position: absolute; left: 0; width: 1200px; height: 446px; overflow: hidden; }
  .carton-panel--one { top: 128px; background: linear-gradient(180deg, var(--sea-light), var(--sea) 60%, #1fa8d0); }
  .carton-panel--two { top: 714px; background: linear-gradient(160deg, var(--aqua-1), var(--aqua-2)); }

  .brand-mark {
    position: absolute; display: flex; flex-direction: column; align-items: center; gap: 10px;
    transform: translateX(-50%);
  }
  .brand-mark__dot { width: 88px; height: 88px; border-radius: 50%; background: var(--navy); }
  .brand-mark__name { font-weight: 600; font-size: 34px; letter-spacing: 3px; color: var(--navy); line-height: 1; }

  .carton-panel--one .brand-mark { left: 256px; top: 36px; }
  .carton-panel--two .brand-mark { left: 268px; top: 22px; }

  .ice-art {
    position: absolute; left: 48px; top: 208px; width: 432px; height: 176px;
    background: radial-gradient(ellipse at 50% 60%, rgba(255,255,255,.9), rgba(220,240,248,.6) 55%, rgba(255,255,255,0) 75%);
  }

  .product-name { position: absolute; text-align: center; color: var(--navy); line-height: 1; }
  .product-name--bold {
    left: 52px; width: 400px; top: 218px;
    font-weight: 800; font-size: 54px; letter-spacing: 3px;
    color: var(--white); -webkit-text-stroke: 3px var(--navy); paint-order: stroke fill;
  }
  .product-name--bold span { display: block; margin-bottom: 0; }
  .product-name--light {
    left: 72px; width: 400px; top: 192px;
    font-weight: 300; font-size: 72px; letter-spacing: 6px;
  }
  .product-name--light span { display: block; margin-bottom: 8px; }

  .photo-catch {
    position: absolute; left: 480px; top: 0; width: 720px; height: 396px;
    background: linear-gradient(120deg, #c9a9a6 0%, #8d8f96 30%, #b46a5a 55%, #9a9ca4 75%, #5f9a4a 100%);
    clip-path: polygon(18% 0, 100% 0, 100% 100%, 10% 100%, 14% 88%, 9% 76%, 13% 64%, 10% 52%, 16% 40%, 12% 28%, 17% 14%);
  }
  .photo-bass {
    position: absolute; left: 424px; top: 30px; width: 776px; height: 366px;
    background: radial-gradient(ellipse at 55% 60%, #6f6a44 0%, #8fa0a0 35%, rgba(220,236,244,.85) 60%, rgba(220,236,244,0) 80%);
  }

  .cold-badge {
    position: absolute; left: 1090px; top: 0; width: 88px; height: 150px;
    background: var(--navy); border: 2px solid var(--white); border-top: 0;
    border-radius: 0 0 12px 12px;
  }
  .cold-badge svg, .cold-mark svg { width: 100%; height: 100%; }
  .cold-mark { position: absolute; left: 1092px; top: 14px; width: 80px; height: 124px; }

  .care-band {
    position: absolute; left: 0; bottom: 0; width: 1200px; height: 50px;
    background: var(--navy-deep); color: var(--white);
    font-weight: 500; font-size: 13.5px; letter-spacing: .6px; line-height: 1.25;
  }
  .care-band__rule { position: absolute; top: 24px; height: 2px; background: var(--white); }
  .care-band__rule--left { left: 0; width: 176px; }
  .care-band__rule--right { left: 1022px; width: 178px; }
  .care-item { position: absolute; top: 0; height: 50px; display: flex; align-items: center; }
  .care-icon { position: absolute; top: 7px; width: 36px; height: 36px; }
  .care-icon svg { width: 100%; height: 100%; }
  .stack-count {
    position: absolute; top: 6px; left: 346px; width: 32px; text-align: center;
    font-size: 21px; font-weight: 500; line-height: 1; border-bottom: 2px solid var(--white);
  }
  .stack-count::after {
    content: ""; display: block; height: 4px; margin-top: 3px; background: var(--white);
    box-shadow: 0 7px 0 var(--white);
  }
</style>
</head>
<body>

<h2 class="option-title option-title--one">Design 01</h2>

<section class="carton-panel carton-panel--one">
  <div class="photo-catch" role="img" aria-label="Photo of fresh whole fish on crushed ice with lettuce and peppers"></div>
  <div class="ice-art" role="img" aria-label="Illustration of ice blocks floating in water"></div>

  <div class="brand-mark">
    <span class="brand-mark__dot"></span>
    <span class="brand-mark__name">VELISA</span>
  </div>

  <h1 class="product-name product-name--bold"><span>FROZEN</span><span>FISH</span></h1>

  <div class="cold-badge">
    <svg viewBox="0 0 88 150" aria-label="Store at minus 18 degrees">
      <g stroke="#fff" stroke-width="3" stroke-linecap="round" fill="none">
        <path d="M24 28v30M11 36l26 14M11 50l26-14"/>
      </g>
      <text x="24" y="80" fill="#fff" font-family="Montserrat, sans-serif" font-size="16" text-anchor="middle">-18</text>
      <g fill="none" stroke="#fff" stroke-width="4">
        <path d="M54 110V38a10 10 0 0 1 20 0v72"/>
        <circle cx="64" cy="120" r="14"/>
      </g>
      <circle cx="64" cy="120" r="6" fill="#fff"/>
      <path d="M64 114V60" stroke="#fff" stroke-width="4"/>
      <path d="M74 50h6M74 62h6M74 74h6M74 86h6M74 98h6" stroke="#fff" stroke-width="2"/>
    </svg>
  </div>

  <div class="care-band">
    <span class="care-band__rule care-band__rule--left"></span>
    <div class="care-icon" style="left:198px">
      <svg viewBox="0 0 36 36" fill="none" stroke="#fff" stroke-width="2.4" stroke-linejoin="round">
        <path d="M18 4l9 5v9l-9 5-9-5V9z"/><path d="M9 9l9 5 9-5M18 14v9"/>
        <path d="M2 20l8 9h6M34 20l-8 9h-6"/>
      </svg>
    </div>
    <div class="care-item" style="left:252px">FROZEN</div>
    <div class="stack-count">10</div>
    <div class="care-item" style="left:394px">Maximum Stackable<br>10 Carton</div>
    <div class="care-icon" style="left:582px">
      <svg viewBox="0 0 36 36" fill="none" stroke="#fff" stroke-width="3.5" stroke-linecap="round">
        <path d="M12 10l5-7 5 7M26 14l5 8h-9M9 28H4l4-8"/>
        <path d="M17 3l-6 10M31 22l-5 9H16M8 20l5 8"/>
      </svg>
    </div>
    <div class="care-item" style="left:634px">Recyleable Material</div>
    <div class="care-icon" style="left:820px">
      <svg viewBox="0 0 36 36"><circle cx="18" cy="18" r="16" fill="none" stroke="#fff" stroke-width="2.4"/><path d="M18 7c5 7 8 11 8 15a8 8 0 0 1-16 0c0-4 3-8 8-15z" fill="#fff"/></svg>
    </div>
    <div class="care-item" style="left:872px">Protect from<br>The Water/Rain</div>
    <span class="care-band__rule care-band__rule--right"></span>
  </div>
</section>

<h2 class="option-title option-title--two">Design 02</h2>

<section class="carton-panel carton-panel--two">
  <div class="photo-bass" role="img" aria-label="Photo of a whole bass fish leaping over ice cubes"></div>

  <div class="brand-mark">
    <span class="brand-mark__dot"></span>
    <span class="brand-mark__name">VELISA</span>
  </div>

  <h1 class="product-name product-name--light"><span>FROZEN</span><span>FISH</span></h1>

  <div class="cold-mark">
    <svg viewBox="0 0 80 124" aria-label="Store at minus 18 degrees">
      <g stroke="#1f3b86" stroke-width="3" stroke-linecap="round" fill="none">
        <path d="M20 8v32M6 16l28 16M6 32l28-16"/>
      </g>
      <text x="22" y="62" fill="#1f3b86" font-family="Montserrat, sans-serif" font-size="17" text-anchor="middle">-18</text>
      <g fill="none" stroke="#1f3b86" stroke-width="4">
        <path d="M50 92V14a10 10 0 0 1 20 0v78"/>
        <circle cx="60" cy="104" r="14"/>
      </g>
      <circle cx="60" cy="104" r="6" fill="#1f3b86"/>
      <path d="M60 98V44" stroke="#1f3b86" stroke-width="4"/>
      <path d="M70 26h6M70 40h6M70 54h6M70 68h6M70 82h6" stroke="#1f3b86" stroke-width="2"/>
    </svg>
  </div>

  <div class="care-band">
    <span class="care-band__rule care-band__rule--left"></span>
    <div class="care-icon" style="left:198px">
      <svg viewBox="0 0 36 36" fill="none" stroke="#fff" stroke-width="2.4" stroke-linejoin="round">
        <path d="M18 4l9 5v9l-9 5-9-5V9z"/><path d="M9 9l9 5 9-5M18 14v9"/>
        <path d="M2 20l8 9h6M34 20l-8 9h-6"/>
      </svg>
    </div>
    <div class="care-item" style="left:252px">FROZEN</div>
    <div class="stack-count">10</div>
    <div class="care-item" style="left:394px">Maximum Stackable<br>10 Carton</div>
    <div class="care-icon" style="left:582px">
      <svg viewBox="0 0 36 36" fill="none" stroke="#fff" stroke-width="3.5" stroke-linecap="round">
        <path d="M12 10l5-7 5 7M26 14l5 8h-9M9 28H4l4-8"/>
        <path d="M17 3l-6 10M31 22l-5 9H16M8 20l5 8"/>
      </svg>
    </div>
    <div class="care-item" style="left:634px">Recyleable Material</div>
    <div class="care-icon" style="left:820px">
      <svg viewBox="0 0 36 36"><circle cx="18" cy="18" r="16" fill="none" stroke="#fff" stroke-width="2.4"/><path d="M18 7c5 7 8 11 8 15a8 8 0 0 1-16 0c0-4 3-8 8-15z" fill="#fff"/></svg>
    </div>
    <div class="care-item" style="left:872px">Protect from<br>The Water/Rain</div>
    <span class="care-band__rule care-band__rule--right"></span>
  </div>
</section>

</body>
</html>
```